A book titled The Raven Left Us A Riddle. It's intended to change peoples perspective of the streets

Title: The Raven Left Us A Riddle
Subtitile: And We Keep On Turning Its Pages. (Doesn't really have to be on the cover, you decide.)
Author: Marvin Quillingsby
Book Size: 6x9 I need a book cover design for my first book. It's a very short book 60-70 pages. It is a book that points out the tricks the devil uses to get people to run the streets. It's meant to destroy some of the patterns that have been set in place in neighborhoods that are considered bad.
I didn't want to tell people what the book was about at all so that whoever came the closest to displaying what I was thinking would be the winner. Since I have given you a snippet of what it is about, I won't lead you any further. Whatever colors, whatever theme, whatever you come up with is totally up to you.

Target Market(s)

18-35 year olds

Requirements
Must have
• At this point I don't want to interfere with the creativity that could come forth. This might be a premature decision on my part. I don't want to say add this or I don't want this. I want it to be as special as I feel the title and the book is. I want it to be compelling enough, and coincide with the title enough that someone has to pick it up to read it.
Nice to have
• At this point I don't want to interfere with the creativity that could come forth. This might be a premature decision on my part. I don't want to say add this or I don't want this.
Should not have

```html
<!DOCTYPE html>
<html lang="en">
<head>
<meta charset="utf-8">
<title>The Raven Left Us A Riddle — Marvin Quillingsby</title>
<link rel="stylesheet" href="https://fonts.googleapis.com/css2?family=Bebas+Neue&family=Oswald:wght@400;500&display=swap">
<style>
  :root {
    --ink-black: #1c1917;
    --ember-red: #b01c0f;
    --blood-red: #c4260f;
    --flame-orange: #e0661a;
    --gold-orange: #f1a321;
    --title-gold: #f2a51f;
    --subtitle-white: #f6eee6;
    --author-brown: #2a1608;
  }
  * { margin: 0; padding: 0; box-sizing: border-box; }
  html, body {
    width: 800px;
    height: 1200px;
    overflow: hidden;
    background: var(--ink-black);
  }
  .book-cover {
    position: relative;
    width: 800px;
    height: 1200px;
    overflow: hidden;
  }
  .cover-painting {
    position: absolute;
    inset: 0;
    width: 800px;
    height: 1200px;
    display: block;
  }
  .cover-title {
    position: absolute;
    top: 134px;
    left: 0;
    width: 800px;
    text-align: center;
    font-family: "Bebas Neue", "Oswald", sans-serif;
    font-weight: 400;
    font-size: 54px;
    line-height: 1;
    letter-spacing: 0.13em;
    padding-left: 0.13em;
    color: var(--title-gold);
    text-transform: uppercase;
  }
  .cover-subtitle {
    position: absolute;
    top: 608px;
    left: 0;
    width: 800px;
    text-align: center;
    font-family: "Oswald", sans-serif;
    font-weight: 500;
    font-size: 19px;
    line-height: 1;
    letter-spacing: 0.12em;
    padding-left: 0.12em;
    color: var(--subtitle-white);
    text-transform: uppercase;
  }
  .cover-author {
    position: absolute;
    top: 1104px;
    left: 0;
    width: 800px;
    text-align: center;
    font-family: "Oswald", sans-serif;
    font-weight: 400;
    font-size: 21px;
    line-height: 1;
    letter-spacing: 0.5em;
    padding-left: 0.5em;
    color: var(--author-brown);
    text-transform: uppercase;
  }
</style>
</head>
<body>
  <main class="book-cover">
    <svg class="cover-painting" viewBox="0 0 800 1200" role="img" aria-label="Abstract painted background: dark charcoal sky over a rough band of deep red brush strokes fading into fiery orange">
      <defs>
        <linearGradient id="paint-fade" x1="0" y1="0" x2="0" y2="1">
          <stop offset="0" stop-color="var(--ink-black)"/>
          <stop offset="0.21" stop-color="var(--ink-black)"/>
          <stop offset="0.28" stop-color="var(--ember-red)"/>
          <stop offset="0.55" stop-color="var(--blood-red)"/>
          <stop offset="0.68" stop-color="var(--flame-orange)"/>
          <stop offset="1" stop-color="var(--gold-orange)"/>
        </linearGradient>
      </defs>
      <rect width="800" height="1200" fill="url(#paint-fade)"/>
    </svg>

    <h1 class="cover-title">The Raven Left Us A Riddle</h1>
    <p class="cover-subtitle">And We Keep On Turning Its Pages.</p>
    <p class="cover-author">Marvin Quillingsby</p>
  </main>
</body>
</html>
```